Branding product image: TOMBEL (Golden Papaya) in Plastic Cup (Ready to Eat)

The product is sliced Fruit in Light syrup
Flavour: TOMBEL (Golden Papaya)
The temporary product name: TOMBEL
I want the product design to be something 'fun', 'natural', and 'colourful'
The design concept could be anything depends on your imagination, but it must be eye catchy and attractive.
Basically, I want you to be creative in designing the logo and the overall graphic design for the label.
The measurement is 20 cm (Length) x 6,5 cm (Height)
The target customers are young and health conscious audiences (10 years - 65 years old).
Create something different. Something extraordinary.
Brief summary about the fruit:
This fruit only grows in certain part of the world. It grows in mountain area that is in tropical climate. The fruit flesh has a yellowish-golden color. It has an extraordinary taste (unlike normal papaya) and it suits very well with any dishes from cold appetizer, white/ red meat, desserts, and cocktails.
I need a packaging design for Fruit Cup productThe product is sliced Fruit in Light syrup.There will be various flavours i.e. apple, lychee, peach, papaya, etc.However, you may design the product using one sample flavour (i.e. papaya) first, as the designs of other flavours could be adjusted afterwards.The temporary product name is: RICCANAI want the product design to be something 'fun', 'natural', and 'colourful'.The design concept could be anything depends on your imagination. Basically, I want you to be creative in designing the logo and the overall graphic design for the label. - Create something different. Something extraordinary -Additional:The measurement is 20cm (Length) x 5cm (Height).The target customers are young audiences (10 years - 35 years old).The product design must stand out in the supermarket shelf.It must be eye catchy and attractive.Thank you,Harold-PLEASE REFER TO DESIGN SAMPLE ATTACHED TO HAVE A BETTER UNDERSTANDING FOR THE PRODUCT CONCEPT- Added Wednesday, September 17, 2014
Project Deadline Extended Reason: Haven't found a good design. Added Friday, September 19, 2014
Project Deadline Extended Reason: Need more time for designers to finalize and perfect the design.Thank you,Harold Added Monday, September 29, 2014
Project Deadline Extended Reason: I haven't found a great design yet. Added Tuesday, February 24, 2015
Reason: Getting better designs now. Still Open to new ideas while refining the latest designs from some designers.
Please do your best in submitting other great designs!

```html
<!DOCTYPE html>
<html lang="en">
<head>
<meta charset="utf-8">
<title>Lupedos Golden Papaya – Cup Label</title>
<link rel="stylesheet" href="https://fonts.googleapis.com/css2?family=Fredoka:wght@500;600&family=Comic+Neue:ital,wght@1,700&family=Open+Sans:wght@400&display=swap">
<style>
  :root {
    --stage: #ececec;
    --label-paper: #f1f1ef;
    --label-paper-edge: #e3e3e0;
    --brand-pink: #c8317a;
    --flavour-purple: #8b2f93;
    --syrup-purple: #9a3fa0;
    --fruit-green: #b7c63c;
    --fruit-orange: #f08a2a;
    --hill-light: #a8d54a;
    --hill-dark: #5fa62a;
    --badge-orange: #f07f1e;
    --badge-text: #ffffff;
    --base-band: #5a4b41;
    --base-text: #e8ddd0;
  }
  * { margin: 0; padding: 0; box-sizing: border-box; }
  html, body { width: 1200px; height: 1000px; overflow: hidden; }
  body {
    background: var(--stage);
    display: flex;
    align-items: center;
    justify-content: center;
  }
  .cup-label {
    position: relative;
    width: 1040px;
    height: 338px;
    background: linear-gradient(180deg, var(--label-paper) 0%, var(--label-paper-edge) 100%);
    overflow: hidden;
  }
  .brand-name {
    position: absolute;
    top: 22px; left: 0; right: 0;
    text-align: center;
    font-family: "Fredoka", sans-serif;
    font-weight: 600;
    font-size: 82px;
    line-height: 1;
    color: var(--brand-pink);
    letter-spacing: 1px;
  }
  .flavour-name {
    position: absolute;
    top: 108px; left: 0; right: 0;
    text-align: center;
    font-family: "Fredoka", sans-serif;
    font-weight: 500;
    font-size: 28px;
    color: var(--flavour-purple);
  }
  .syrup-note {
    position: absolute;
    top: 150px; left: 50%;
    transform: translateX(-50%);
    padding: 3px 10px;
    border-top: 2px dotted var(--syrup-purple);
    border-bottom: 2px dotted var(--syrup-purple);
    font-family: "Comic Neue", sans-serif;
    font-style: italic;
    font-weight: 700;
    font-size: 14px;
    color: var(--syrup-purple);
    white-space: nowrap;
  }
  .fruit-artwork {
    position: absolute;
    top: 186px; left: 50%;
    width: 130px; height: 96px;
    transform: translateX(-50%);
    border-radius: 48% 48% 40% 40%;
    background: radial-gradient(circle at 62% 55%, var(--fruit-orange) 0%, #f5a54a 40%, var(--fruit-green) 75%);
  }
  .burst-lines {
    position: absolute;
    top: 176px; left: 50%;
    transform: translateX(-50%);
  }
  .hills {
    position: absolute;
    left: 0; right: 0; bottom: 28px;
    height: 56px;
  }
  .flavour-badge {
    position: absolute;
    bottom: 34px; left: 50%;
    transform: translateX(-50%);
    width: 104px; height: 50px;
    border-radius: 46% 54% 50% 50% / 60% 55% 45% 40%;
    background: var(--badge-orange);
    text-align: center;
    font-family: "Fredoka", sans-serif;
    font-weight: 600;
    color: var(--badge-text);
    padding-top: 5px;
    line-height: 1;
  }
  .flavour-badge .badge-title { display: block; font-size: 20px; }
  .flavour-badge .badge-sub { display: block; font-size: 14px; margin-top: 2px; }
  .base-band {
    position: absolute;
    left: 0; right: 0; bottom: 0;
    height: 28px;
    background: var(--base-band);
    text-align: center;
    font-family: "Open Sans", sans-serif;
    font-size: 14px;
    line-height: 28px;
    letter-spacing: 0.5px;
    color: var(--base-text);
  }
</style>
</head>
<body>
  <section class="cup-label">
    <h1 class="brand-name">Lupedos</h1>
    <p class="flavour-name">Golden Papaya</p>
    <p class="syrup-note">in light syrup</p>

    <svg class="burst-lines" width="210" height="60" viewBox="0 0 210 60" aria-hidden="true">
      <g stroke="var(--fruit-orange)" stroke-width="2" stroke-linecap="round">
        <line x1="22" y1="14" x2="34" y2="22"/>
        <line x1="14" y1="32" x2="28" y2="33"/>
        <line x1="188" y1="14" x2="176" y2="22"/>
        <line x1="196" y1="32" x2="182" y2="33"/>
      </g>
    </svg>

    <div class="fruit-artwork" role="img" aria-label="Whole golden papaya beside a halved papaya showing orange flesh and dark seeds"></div>

    <svg class="hills" width="1040" height="56" viewBox="0 0 1040 56" preserveAspectRatio="none" role="img" aria-label="Rolling green grassy hills">
      <defs>
        <linearGradient id="hillFill" x1="0" y1="0" x2="0" y2="1">
          <stop offset="0" stop-color="var(--hill-light)"/>
          <stop offset="1" stop-color="var(--hill-dark)"/>
        </linearGradient>
      </defs>
      <path d="M0 56 L0 44 Q260 30 420 20 Q520 0 620 20 Q780 30 1040 44 L1040 56 Z" fill="url(#hillFill)"/>
    </svg>

    <div class="flavour-badge">
      <span class="badge-title">Papaya</span>
      <span class="badge-sub">Flavour</span>
    </div>

    <footer class="base-band">NET WT 6 Oz (170g)</footer>
  </section>
</body>
</html>
```